Lotus Reed Kitchen Road Billboard

Road Billboard I need all of this information on it
Authentic Thai Food Bangkok Style
6.5 Miles on the right
4172 Marlow Rd Pelham NC
828-555-0147

```html
<!DOCTYPE html>
<html lang="en">
<head>
<meta charset="utf-8">
<title>Lotus Reed Kitchen – Road Billboard</title>
<link href="https://fonts.googleapis.com/css2?family=Poppins:wght@600;700;800&family=Oswald:wght@700&display=swap" rel="stylesheet">
<style>
  :root {
    --navy: #1b2a3d;
    --orange: #f5981f;
    --white: #ffffff;
    --stage: #e9edf1;
    --plate-light: #f4efe6;
    --plate-mid: #d98a3c;
  }
  html, body {
    margin: 0;
    width: 1200px;
    height: 800px;
    overflow: hidden;
    background: var(--stage);
  }
  .billboard {
    position: absolute;
    left: 20px;
    top: 120px;
    width: 1160px;
    height: 560px;
    background: var(--white);
    overflow: hidden;
    font-family: "Poppins", sans-serif;
    color: var(--navy);
  }
  .billboard-art {
    position: absolute;
    inset: 0;
  }
  .copy {
    position: absolute;
    left: 30px;
    top: 62px;
    width: 600px;
    display: flex;
    flex-direction: column;
    align-items: center;
    text-align: center;
    white-space: nowrap;
  }
  .headline {
    margin: 0;
    display: flex;
    flex-direction: column;
    align-items: center;
  }
  .headline-kicker {
    color: var(--orange);
    font-weight: 700;
    font-size: 54px;
    line-height: 1;
    letter-spacing: 1px;
  }
  .headline-main {
    font-weight: 800;
    font-size: 92px;
    line-height: 1;
    letter-spacing: -1px;
    margin-top: 2px;
  }
  .style-pill {
    margin-top: 6px;
    padding: 2px 24px;
    border-radius: 20px;
    background: var(--orange);
    color: var(--white);
    font-weight: 800;
    font-size: 34px;
    line-height: 1.2;
  }
  .directions {
    margin: 20px 0 0;
    font-weight: 800;
    font-size: 34px;
    line-height: 1.1;
  }
  .address-block {
    margin-top: 12px;
    width: 320px;
  }
  .divider {
    position: relative;
    height: 1px;
    background: var(--navy);
  }
  .divider::after {
    content: "";
    position: absolute;
    left: 50%;
    top: -4px;
    width: 8px;
    height: 8px;
    margin-left: -4px;
    background: var(--orange);
    transform: rotate(45deg);
  }
  .address {
    margin: 10px 0;
    font-weight: 700;
    font-size: 21px;
    line-height: 1.2;
  }
  .call {
    margin: 16px 0 0;
    font-family: "Oswald", sans-serif;
    font-weight: 700;
    font-size: 64px;
    line-height: 1;
  }
  .call-label { color: var(--orange); }
  .call-number { color: var(--navy); }
</style>
</head>
<body>
  <main class="billboard">
    <svg class="billboard-art" width="1160" height="560" viewBox="0 0 1160 560">
      <defs>
        <radialGradient id="plate-fill" cx="50%" cy="50%" r="50%">
          <stop offset="0%" stop-color="var(--plate-mid)"/>
          <stop offset="55%" stop-color="#e6b57a"/>
          <stop offset="85%" stop-color="var(--plate-light)"/>
          <stop offset="100%" stop-color="#8a4a2a"/>
        </radialGradient>
      </defs>
      <polygon class="accent-band" points="800,0 1160,0 930,560 580,560" fill="var(--navy)"/>
      <path class="ring-thick" d="M 753 67 A 235 235 0 0 1 1050 421" fill="none" stroke="var(--orange)" stroke-width="38"/>
      <path class="ring-thin" d="M 703 71 A 260 260 0 1 0 1000 495" fill="none" stroke="var(--orange)" stroke-width="6"/>
      <circle class="ring-dot" cx="703" cy="71" r="15" fill="var(--orange)"/>
      <circle class="ring-dot" cx="1000" cy="495" r="15" fill="var(--orange)"/>
      <circle class="dish-photo" cx="870" cy="270" r="205" fill="url(#plate-fill)" role="img" aria-label="Plate of Thai stir-fried shrimp with noodles, crushed peanuts, lettuce, broccoli, herbs and a lime wedge"/>
    </svg>

    <div class="copy">
      <h1 class="headline">
        <span class="headline-kicker">AUTHENTIC</span>
        <span class="headline-main">THAI FOOD</span>
        <span class="style-pill">BANGKOK STYLE</span>
      </h1>

      <p class="directions">6.5 MILES ON THE RIGHT</p>

      <div class="address-block">
        <div class="divider"></div>
        <p class="address">4172 Marlow Rd Pelham NC</p>
        <div class="divider"></div>
      </div>

      <p class="call"><span class="call-label">Call:</span> <span class="call-number">828-555-0147</span></p>
    </div>
  </main>
</body>
</html>
```